Dale Morrikan Plumbing and Heating

Need a card design for a plumbing and heating company that does service and repair, remodels, and plumbing in new construction. Please add following on back side of card; Boilers, Water heaters, Gas lines, Sump pumps, Toilet repairs, Faucet repairs, Pipe thawing, Radiant heating, New construction, Remodels.

Industry/Entity Type

Plumber

Contact Information for Business Card

Was thinking white gloss card with colored logo in middle or black glossy card with silver logo in middle. Just a thought but very open to other designs.

Requirements
Must have
• Need following on front of card;
• P(203) 321-8689
• C(203) 232-9069
• Dale Morrikan 275 Larkwell St West, Stamford, Ct 06214
• service@DrainHearth.example (plumbing in blue, heating in red)
• www.DrainHearth.example (plumbing in blue, heating in red)
• Fully Licensed and Insured
Nice to have
• Elegant design

```html
<!DOCTYPE html>
<html lang="en">
<head>
<meta charset="utf-8">
<title>Dale Morrikan Plumbing and Heating – Business Card</title>
<link href="https://fonts.googleapis.com/css2?family=Exo+2:wght@400;600;700&family=Montserrat:wght@400;600&display=swap" rel="stylesheet">
<style>
  :root {
    --backdrop: #2b2b2b;
    --card-black: #111214;
    --card-black-edge: #1d1e21;
    --card-white: #ffffff;
    --card-white-shade: #eef0f2;
    --brand-blue: #2b3a9c;
    --brand-red: #d2262c;
    --silver: #c9ccd1;
    --text-grey: #6d6f73;
    --list-grey: #a9abb0;
    --divider-blue: #5b86c9;
  }
  * { box-sizing: border-box; margin: 0; padding: 0; }
  html, body { width: 1200px; height: 768px; overflow: hidden; }
  body {
    background: var(--backdrop);
    font-family: "Exo 2", sans-serif;
    position: relative;
  }
  .card {
    position: absolute;
    top: 234px;
    width: 525px;
    height: 300px;
    border-radius: 18px;
    overflow: hidden;
  }
  /* Back side */
  .card-back {
    left: 50px;
    background: linear-gradient(160deg, var(--card-black-edge), var(--card-black) 60%);
    color: #fff;
    text-align: center;
  }
  .back-brand {
    position: absolute;
    top: 78px; left: 0; right: 0;
    display: flex; align-items: center; justify-content: center; gap: 12px;
    font-weight: 600; font-size: 26px; letter-spacing: 1px;
    color: var(--silver);
  }
  .brand-dot {
    width: 14px; height: 14px; border-radius: 50%;
    background: var(--silver);
  }
  .back-licence {
    position: absolute; top: 150px; left: 0; right: 0;
    font-family: "Montserrat", sans-serif;
    font-weight: 600; font-size: 17px;
  }
  .service-list {
    position: absolute; top: 186px; left: 40px; right: 40px;
    font-family: "Montserrat", sans-serif;
    font-size: 12.5px; line-height: 22px;
    color: var(--list-grey);
    list-style: none;
  }
  .service-list li { display: inline; }
  .service-list li + li::before {
    content: "";
    display: inline-block;
    width: 6px; height: 6px; border-radius: 50%;
    background: var(--list-grey);
    margin: 0 7px 1px 5px;
  }
  /* Front side */
  .card-front {
    left: 625px;
    background: linear-gradient(135deg, var(--card-white) 55%, var(--card-white-shade));
  }
  .front-brand {
    position: absolute; top: 52px; right: 34px;
    text-align: right;
  }
  .front-brand-name {
    display: flex; align-items: center; justify-content: flex-end; gap: 8px;
    font-weight: 700; font-size: 20px; line-height: 1.1;
    color: var(--brand-blue);
    text-transform: uppercase;
  }
  .front-brand-name .brand-dot { background: var(--brand-blue); width: 12px; height: 12px; }
  .brand-url {
    margin-top: 6px;
    font-size: 11px; font-weight: 600;
    color: var(--text-grey);
  }
  .blue { color: var(--brand-blue); }
  .red { color: var(--brand-red); }
  .person { position: absolute; left: 30px; top: 140px; }
  .person-name { font-weight: 600; font-size: 21px; color: var(--brand-blue); }
  .person-role { font-size: 14px; color: var(--brand-red); margin-top: 1px; }
  .contacts { position: absolute; left: 30px; top: 196px; font-size: 14px; color: var(--text-grey); }
  .contact-line { display: flex; align-items: center; gap: 9px; height: 22px; }
  .contact-line svg { width: 12px; height: 14px; fill: var(--brand-blue); }
  .email { position: absolute; left: 30px; top: 246px; font-size: 13.5px; color: var(--text-grey); }
  .divider {
    position: absolute; left: 262px; top: 208px;
    width: 1.5px; height: 58px; background: var(--divider-blue);
  }
  .address {
    position: absolute; left: 280px; top: 210px;
    font-size: 14px; line-height: 19px; color: var(--text-grey);
  }
</style>
</head>
<body>
  <section class="card card-back" aria-label="Card back">
    <div class="back-brand"><span class="brand-dot"></span>Dale Morrikan Plumbing and Heating</div>
    <p class="back-licence">Fully Licensed and Insured</p>
    <ul class="service-list">
      <li>Boilers</li><li>Water heaters</li><li>Gas lines</li><li>Sump pumps</li><li>Toilet repairs</li><li>Faucet repairs</li><li>Pipe thawing</li><li>Radiant heating</li><li>New construction</li><li>Remodels</li>
    </ul>
  </section>

  <section class="card card-front" aria-label="Card front">
    <div class="front-brand">
      <div class="front-brand-name"><span class="brand-dot"></span>Dale Morrikan<br>Plumbing and Heating</div>
      <div class="brand-url">www.<span class="blue">Drain</span><span class="red">Hearth</span>.example</div>
    </div>

    <div class="person">
      <div class="person-name">Evan Hollis</div>
      <div class="person-role">CEO/Founder</div>
    </div>

    <div class="contacts">
      <div class="contact-line">
        <svg viewBox="0 0 12 14" aria-hidden="true"><path d="M2 0h3l1 3.5-2 1.2c.8 2 2 3.4 3.7 4.3l1.3-1.9L12 8.5V12c0 1-1 2-2 2C4.5 13.5 0 8.5 0 2 0 1 1 0 2 0z"/></svg>
        <span>(203) 555-0147</span>
      </div>
      <div class="contact-line">
        <svg viewBox="0 0 12 14" aria-hidden="true"><path d="M2 0h8a1.5 1.5 0 0 1 1.5 1.5v11A1.5 1.5 0 0 1 10 14H2A1.5 1.5 0 0 1 .5 12.5v-11A1.5 1.5 0 0 1 2 0zm0.5 2v9h7V2z"/></svg>
        <span>(203) 555-0183</span>
      </div>
    </div>
    <div class="email">service@<span class="blue">Drain</span><span class="red">Hearth</span>.example</div>

    <div class="divider"></div>
    <address class="address" style="font-style:normal">
      Dale Morrikan<br>
      275 Larkwell St West<br>
      Stamford, Ct 06214
    </address>
  </section>
</body>
</html>
```